Poster Design Project

We need a poster design for a "Karaoke Night" at a bar. Should appeal to a young crowd. Graphics should be musically themed.

Should include info:

When: July 29, 2013 from 7PM to 2AM
Where: Halvern's Pub
1/2 Off on draft beer until 9:30PM
Updates

Project Deadline Extended
Reason: Checking on copyright issues

Target Market(s)

U.S. Market ages 21 to 30, upscale and female

Industry/Entity Type

Crowd

Requirements
Must have
• Needs to be 2 by 3 aspect ratio. Must look good at 3 feet tall (render well at high resolution of 8100 by 5400).
Nice to have
• Do something create with the title "Karaoke Night".

```html
<!DOCTYPE html>
<html lang="en">
<head>
<meta charset="utf-8">
<title>Karaoke Night at Halvern's Pub</title>
<link rel="stylesheet" href="https://fonts.googleapis.com/css2?family=Saira+Stencil+One&family=Quicksand:wght@300&display=swap">
<style>
  :root {
    --page: #ffffff;
    --poster: #58258a;
    --footer-text: #d9c8ee;
    --c-indigo: #3a2fa0;
    --c-moss: #4f7a52;
    --c-slate: #6f9bb5;
    --c-magenta: #b1128a;
    --c-wine: #7c1746;
    --c-ochre: #b27a38;
    --c-rust: #a3443a;
    --c-steel: #5f6fa0;
    --c-lilac: #7560b0;
    --c-rose: #c0355a;
    --c-olive: #5f7a3c;
    --c-orchid: #a23a98;
    --c-royal: #5660d8;
    --c-sky: #3f8fea;
    --c-plum: #8a3fa8;
    --c-gold: #b8962e;
    --c-crimson: #a12a3c;
    --c-teal: #5b8c9c;
    --c-fuchsia: #c21fd6;
    --c-berry: #8c2e6a;
    --c-mauve: #9c6a80;
    --c-violet: #9a2ab8;
    --c-green: #1f8a2e;
    --c-lime: #c4c21a;
    --c-blue: #1a2fc0;
    --c-grey: #8c8c8c;
  }
  html, body {
    margin: 0;
    width: 900px;
    height: 1200px;
    overflow: hidden;
    background: var(--page);
  }
  .poster {
    position: absolute;
    left: 48px;
    top: 0;
    width: 800px;
    height: 1200px;
    overflow: hidden;
    background: var(--poster);
  }
  .title, .venue, .when {
    position: absolute;
    margin: 0;
    font-family: "Saira Stencil One", "Arial Black", sans-serif;
    font-weight: 400;
    letter-spacing: -3px;
  }
  .title {
    right: 24px;
    top: 12px;
    text-align: right;
    font-size: 124px;
    line-height: 104px;
  }
  .venue {
    left: 26px;
    top: 346px;
    text-align: left;
    font-size: 124px;
    line-height: 110px;
  }
  .when {
    right: 24px;
    top: 814px;
    text-align: right;
    font-size: 88px;
    line-height: 94px;
  }
  .title span, .venue span, .when span { display: inline-block; }
  .gap { width: 30px; }
  .offer {
    position: absolute;
    left: 0;
    right: 0;
    top: 1072px;
    margin: 0;
    text-align: center;
    font-family: "Quicksand", "Helvetica Neue", sans-serif;
    font-weight: 300;
    font-size: 40px;
    color: var(--footer-text);
  }
</style>
</head>
<body>
  <main class="poster">
    <h1 class="title">
      <span style="color:var(--c-indigo)">K</span><span style="color:var(--c-moss)">a</span><span style="color:var(--c-slate)">r</span><span style="color:var(--c-magenta)">-</span><br>
      <span style="color:var(--c-wine)">a</span><span style="color:var(--c-ochre)">o</span><span style="color:var(--c-rust)">k</span><span style="color:var(--c-steel)">e</span><br>
      <span style="color:var(--c-lilac)">N</span><span style="color:var(--c-rose)">i</span><span style="color:var(--c-olive)">g</span><span style="color:var(--c-orchid)">h</span><span style="color:var(--c-royal)">t</span><span style="color:var(--c-sky)">:</span>
    </h1>

    <p class="venue">
      <span style="color:var(--c-plum)">a</span><span style="color:var(--c-gold)">t</span><span style="color:var(--c-ochre)">:</span><br>
      <span style="color:var(--c-crimson)">H</span><span style="color:var(--c-indigo)">a</span><span style="color:var(--c-teal)">l</span><span style="color:var(--c-crimson)">-</span><br>
      <span style="color:var(--c-steel)">v</span><span style="color:var(--c-fuchsia)">e</span><span style="color:var(--c-berry)">r</span><span style="color:var(--c-teal)">n</span><span style="color:var(--c-gold)">'</span><span style="color:var(--c-berry)">s</span><br>
      <span style="color:var(--c-mauve)">P</span><span style="color:var(--c-rust)">u</span><span style="color:var(--c-violet)">b</span>
    </p>

    <p class="when">
      <span style="color:var(--c-rust)">2</span><span style="color:var(--c-moss)">9</span><span class="gap"></span><span style="color:var(--c-ochre)">J</span><span style="color:var(--c-steel)">u</span><span style="color:var(--c-plum)">l</span><span style="color:var(--c-royal)">y</span><span class="gap"></span><span style="color:var(--c-rose)">'</span><span style="color:var(--c-green)">1</span><span style="color:var(--c-lime)">3</span><br>
      <span style="color:var(--c-blue)">7</span><span style="color:var(--c-fuchsia)">p</span><span style="color:var(--c-rust)">m</span><span class="gap"></span><span style="color:var(--c-grey)">-</span><span class="gap"></span><span style="color:var(--c-green)">2</span><span style="color:var(--c-gold)">a</span><span style="color:var(--c-crimson)">m</span>
    </p>

    <p class="offer">50% off on draft beer until 9:30pm</p>
  </main>
</body>
</html>
```